Labels/logo for luxury bath products

I am developing a range of luxury bath foams - aimed at the top end of the luxury market. My company name is VEM (very basic website can be seen at www.vemarton.example).

I am looking for a label design for the front of the bottle, which should incorporate the VEM logo as per the website (file attached), but embedded within a more intricate label design. I provide a link to a picture of the bottle below.

The bath foam will come in four fragrances: Vetiver, Sandalwood, Jasmine and Neroli. The label should include the fragrance name. So the label must include the brand name 'VEM' and the name of the fragrance - e.g. Sandalwood Bath Foam, Neroli Bath Foam, etc.

The products are aimed at both the male and female market and so shouldn't be too feminine.

A brand to take inspiration from is Lune Bravière: http://www.lunebraviere.example/ - I like the labels that they use on their products, which is a gold embossed crest, which they use as the label for their products. I am not referring to their font, but to their label design - I like the embossed label, and am quite keen on metallics.

Conversely, I would like to add a contemporary edge to this design - I like the striping and contemporary fonts on this design: http://www.hadley-frost.example/images/fac83.jpg

My brand also harnesses the powers of natural flower ingredients, and so I am inspired by the products of Quenby - quenby.example. This labelling is more clinical and scientific.

Ideally I would like a label which combines these elements - i.e. a luxury label with a contemporary feel, that incorporate the scientific nature of the product.

The design needs to communicate high end luxury. The bottle is however apothecary style, and a nod to science and botany would be good. I would however like a bold approach to this design - it is a modern brand.

The bottle being used for the product can be seen at: http://www.tavel-vitro.example/en/product-groups/8-Apothecary-bottles - these are extremely expensive bottles and the label needs to reflect this quality. These bottles are traditional in design, but incorporate high end glassware technology to preserve the integrity of the natural ingredients. Therefore the product is a mix of old and new, and the label could also reflect this. The colour of the glass is very deep purple.

The front label does not need information such as weight/volume - it purely needs a label which will recognise it as the VEM brand, with the product name. I am looking for a high quality label, which is unique. I am happy to print embossed labels and to use foils on my labels.

Please do not be boring! I appreciate I have given a variety of influences, so summarise the requirements are a mix of:

a bold design
contemporary
luxury

The label must include NO slogans.

I am looking to build a relationship with a graphic designer for packaging and website design requirements so this will be the first of many projects.

Target Market(s)

Luxury end of market - clientele will like luxury and will pay for the highest quality ingredients in the product, but will also appreciate the botanical nature of the product.

Industry/Entity Type

Graphic Designer

Requirements
Must have
• Must include the company name, VEM, although this doesn't need to be particularly prominent. And the product name, e.g. Sandalwood.
Nice to have
• It should combine luxury, but with recognition of the science behind the product.
Should not have
• No slogans, minimal wording on the front label. No other wording other than company name and product name. No primary colours.

```html
<!DOCTYPE html>
<html lang="en">
<head>
<meta charset="utf-8">
<title>VEM Bath Foam Labels</title>
<link rel="stylesheet" href="https://fonts.googleapis.com/css2?family=Great+Vibes&family=Libre+Baskerville:wght@400;700&display=swap">
<style>
  :root {
    --page: #ffffff;
    --label-black: #0b0b0c;
    --gold-light: #f6e27a;
    --gold-mid: #d9b23c;
    --gold-deep: #a9801f;
    --ink: #111111;
    --cream: #f4f1ea;
    --vetiver: #3fbf2a;
    --jasmine: #ffffff;
    --neroli: #4a2ee0;
    --sandalwood: #8a5a2b;
  }
  * { box-sizing: border-box; margin: 0; padding: 0; }
  html, body {
    width: 1200px;
    height: 900px;
    overflow: hidden;
    background: var(--page);
  }
  .label-range {
    width: 1200px;
    height: 900px;
    display: flex;
    align-items: center;
    justify-content: center;
    gap: 70px;
  }
  .label {
    width: 200px;
    height: 390px;
    border-radius: 12px;
    overflow: hidden;
    background: var(--label-black);
    display: flex;
    flex-direction: column;
  }
  .label__head {
    position: relative;
    height: 186px;
    flex: none;
  }
  .label__stripe,
  .label__foil {
    position: absolute;
    left: 0;
    right: 0;
    top: 0;
    border-radius: 0 0 50% 50% / 0 0 14px 14px;
  }
  .label__stripe { height: 186px; }
  .label__foil {
    height: 172px;
    background: linear-gradient(135deg, var(--gold-deep) 0%, var(--gold-light) 35%, var(--gold-mid) 55%, var(--gold-light) 75%, var(--gold-deep) 100%);
    display: flex;
    align-items: center;
    justify-content: center;
  }
  .brand-name {
    font-family: "Libre Baskerville", Georgia, serif;
    font-weight: 700;
    font-size: 32px;
    color: var(--ink);
    letter-spacing: 0.5px;
  }
  .label--vetiver .label__stripe, .label--vetiver .product-type__dot { background: var(--vetiver); }
  .label--jasmine .label__stripe, .label--jasmine .product-type__dot { background: var(--jasmine); }
  .label--neroli .label__stripe, .label--neroli .product-type__dot { background: var(--neroli); }
  .label--sandalwood .label__stripe, .label--sandalwood .product-type__dot { background: var(--sandalwood); }
  .label__panel {
    flex: 1;
    display: flex;
    flex-direction: column;
    align-items: center;
    padding-top: 22px;
    color: var(--cream);
  }
  .product-name {
    font-family: "Great Vibes", cursive;
    font-weight: 400;
    font-size: 48px;
    line-height: 0.95;
    text-align: center;
  }
  .product-type {
    margin-top: 8px;
    font-family: "Libre Baskerville", Georgia, serif;
    font-size: 15px;
    display: flex;
    align-items: center;
    gap: 8px;
  }
  .product-type__dot {
    width: 7px;
    height: 7px;
    border-radius: 50%;
  }
</style>
</head>
<body>
  <main class="label-range">
    <article class="label label--vetiver">
      <div class="label__head"><div class="label__stripe"></div><div class="label__foil"><span class="brand-name">VEM</span></div></div>
      <div class="label__panel">
        <h2 class="product-name">Vetiber</h2>
        <p class="product-type">Bath<span class="product-type__dot"></span>Foam</p>
      </div>
    </article>
    <article class="label label--jasmine">
      <div class="label__head"><div class="label__stripe"></div><div class="label__foil"><span class="brand-name">VEM</span></div></div>
      <div class="label__panel">
        <h2 class="product-name">Jasmine</h2>
        <p class="product-type">Bath<span class="product-type__dot"></span>Foam</p>
      </div>
    </article>
    <article class="label label--neroli">
      <div class="label__head"><div class="label__stripe"></div><div class="label__foil"><span class="brand-name">VEM</span></div></div>
      <div class="label__panel">
        <h2 class="product-name">Neroli</h2>
        <p class="product-type">Bath<span class="product-type__dot"></span>Foam</p>
      </div>
    </article>
    <article class="label label--sandalwood">
      <div class="label__head"><div class="label__stripe"></div><div class="label__foil"><span class="brand-name">VEM</span></div></div>
      <div class="label__panel">
        <h2 class="product-name">Sandal<br>wood</h2>
        <p class="product-type">Bath<span class="product-type__dot"></span>Foam</p>
      </div>
    </article>
  </main>
</body>
</html>
```